Recruiting agency looking for a newsletter design

We need to design a newsletter that will be sent by e-mail to our clients database. This communication announces a new milestone for our company.

We need it to convey high professionalism, elegance ad luxury. It needs to catch the reader’s attention.

The background needs to be light shiny silver, not flat gray, not dark silver. Some effects can give dimension to the content. We need a very impactful communication.

You will find attached:

- The content that needs to appear on the newsletter
- Pictures “moodboard” that you can take into consideration for the overall “atmosphere” and “emotion” that the design needs to convey. Please DO NOT include any of these images in the newsletter itself. They are just here to help you get the idea of the type of image we want to convey as a company with this communication.
- Company logo
- Please note that I will provide you later on with a URL link to include to the newsletter.

```html
<!DOCTYPE html>
<html lang="en">
<head>
<meta charset="UTF-8">
<title>Vale &amp; Associates – 2021 New Fees</title>
<link rel="stylesheet" href="https://fonts.googleapis.com/css2?family=Montserrat:wght@400;500;700;800&family=Open+Sans:wght@400&display=swap">
<style>
  :root {
    --page-bg: #e1e1e1;
    --ink: #0b0b0b;
    --accent: #d3123e;
    --card-border: #ffffff;
    --silver-light: #fbfbfb;
    --silver-mid: #e6e6e6;
    --silver-deep: #cfcfcf;
    --divider: #bdbdbd;
    --tile: #ffffff;
  }
  * { box-sizing: border-box; margin: 0; padding: 0; }
  html, body {
    width: 680px; height: 1200px; overflow: hidden;
    background: var(--page-bg);
    font-family: "Montserrat", Arial, sans-serif;
    color: var(--ink);
  }
  .canvas { position: relative; width: 680px; height: 1200px; }

  .newsletter {
    position: absolute; left: 80px; top: 80px;
    width: 520px; height: 1024px;
    border: 2px solid var(--card-border);
    background: radial-gradient(ellipse at 55% 10%, var(--silver-light) 0%, var(--silver-mid) 45%, var(--silver-deep) 100%);
    box-shadow: 0 6px 28px rgba(0,0,0,0.18);
    overflow: hidden;
  }

  .brand {
    position: absolute; left: 0; top: 0; width: 100%; height: 164px;
    border-bottom: 1px solid var(--divider);
    display: flex; align-items: flex-end; justify-content: center;
    padding-bottom: 36px; gap: 10px;
  }
  .brand-mark { width: 12px; height: 12px; border-radius: 50%; background: var(--ink); }
  .brand-name {
    font-weight: 700; font-size: 20px; letter-spacing: 3px;
    text-transform: uppercase; color: var(--ink);
  }

  .headline { position: absolute; left: 0; width: 100%; text-align: center; }
  .headline-year { top: 178px; font-size: 82px; font-weight: 800; line-height: 1; letter-spacing: -2px; }
  .headline-title { top: 346px; font-size: 38px; font-weight: 500; line-height: 1; top: 270px; }

  .fees {
    position: absolute; left: 0; top: 333px; width: 100%; height: 400px;
  }
  .fees-photo {
    position: absolute; inset: 0;
    background:
      linear-gradient(100deg, rgba(40,55,70,0.9) 0%, rgba(40,55,70,0) 22%),
      linear-gradient(180deg, #6fb4c6 0%, #a9b9c1 30%, #8a8679 55%, #b59a72 75%, #5f5a52 100%);
  }
  .fee-tile {
    position: absolute; top: 84px; width: 232px; height: 231px;
    background: var(--tile); text-align: center;
    padding-top: 26px;
  }
  .fee-tile--executive { left: 14px; }
  .fee-tile--general { left: 274px; }
  .fee-icon { display: block; margin: 0 auto; height: 34px; }
  .fee-label {
    margin-top: 12px; color: var(--accent);
    font-size: 22px; font-weight: 400; line-height: 31px;
  }
  .fee-rate {
    margin-top: 4px; font-size: 78px; font-weight: 800;
    line-height: 1; letter-spacing: -2px;
  }

  .invite { position: absolute; left: 0; top: 786px; width: 100%; text-align: center; }
  .invite-line { font-size: 29px; font-weight: 500; line-height: 43px; }
  .invite-line strong { font-weight: 800; }
  .more-info { margin-top: 22px; font-size: 24px; font-weight: 400; line-height: 32px; }
  .cta {
    display: inline-block; color: var(--accent); font-size: 24px; font-weight: 700;
    text-decoration: none; border-bottom: 2px solid var(--accent); line-height: 26px;
  }

  .copyright {
    position: absolute; left: 0; top: 1146px; width: 100%; text-align: center;
    font-family: "Open Sans", Arial, sans-serif; font-size: 13px; color: #222;
  }
</style>
</head>
<body>
<div class="canvas">
  <main class="newsletter">
    <header class="brand">
      <span class="brand-mark"></span>
      <span class="brand-name">Vale &amp; Associates</span>
    </header>

    <h1 class="headline headline-year">2021</h1>
    <h2 class="headline headline-title">NEW ERA-NEW FEES</h2>

    <section class="fees">
      <div class="fees-photo" role="img" aria-label="Upward view of modern skyscrapers against a teal sky, lit in warm gold"></div>

      <div class="fee-tile fee-tile--executive">
        <svg class="fee-icon" viewBox="0 0 52 34" width="52" aria-hidden="true">
          <circle cx="26" cy="8" r="7"/>
          <circle cx="10" cy="12" r="5.5"/>
          <circle cx="42" cy="12" r="5.5"/>
          <path d="M14 34 Q14 18 26 18 Q38 18 38 34 Z"/>
          <path d="M0 31 Q0 20 10 20 Q14 20 15 22 Q12 26 12 31 Z"/>
          <path d="M52 31 Q52 20 42 20 Q38 20 37 22 Q40 26 40 31 Z"/>
        </svg>
        <p class="fee-label">Top managers<br>Executives</p>
        <p class="fee-rate">25%</p>
      </div>

      <div class="fee-tile fee-tile--general">
        <svg class="fee-icon" viewBox="0 0 28 32" width="28" aria-hidden="true">
          <rect x="6" y="0" width="4" height="7" rx="1"/>
          <rect x="18" y="0" width="4" height="7" rx="1"/>
          <path d="M2 4 H26 a2 2 0 0 1 2 2 V30 a2 2 0 0 1 -2 2 H2 a2 2 0 0 1 -2 -2 V6 a2 2 0 0 1 2 -2 Z M3 13 V29 H25 V13 Z"/>
          <rect x="5" y="15" width="5" height="5"/><rect x="11.5" y="15" width="5" height="5"/><rect x="18" y="15" width="5" height="5"/>
          <rect x="5" y="22" width="5" height="5"/><rect x="11.5" y="22" width="5" height="5"/><rect x="18" y="22" width="5" height="5"/>
        </svg>
        <p class="fee-label">All other<br>appointments</p>
        <p class="fee-rate">21%</p>
      </div>
    </section>

    <section class="invite">
      <p class="invite-line"><strong>JOIN US</strong> in shaping the<br>future of recruitment</p>
      <p class="more-info">For more information</p>
      <a class="cta" href="#">CLICK HERE</a>
    </section>
  </main>

  <footer class="copyright">Copyright &copy; 2020 &nbsp;Vale &amp; Associates. &nbsp;All rights reserved.</footer>
</div>
</body>
</html>
```